2017 New Year Membership Sale

I require a flyer to be designed for a mail box drop.

We are a 24/7 Gym and will be running a sale in January. No Joining Fee, Flexible membership options.

We are also going to have an open day on Saturday the 21st of January, everyone is welcome. Supplement samples and information. Free health measurements. Free starter PT pack if you join on the day.

We offer a 24/7 DIY gym as well as a comprehensive Personal Training Studio.

I have included the design I used last year.

Target Market(s)

Potential Members of all ages.

Industry/Entity Type

Gym

Requirements
Must have
• Our Address, Phone Number.
• Staffed Hours;
• Mon-Thur: 12pm - 7pm
• Fri-Sat: 8am - 1pm

```html
<!DOCTYPE html>
<html lang="en">
<head>
<meta charset="utf-8">
<title>Huge Membership Sale – Pacer Fitness Ashgrove</title>
<link rel="stylesheet" href="https://fonts.googleapis.com/css2?family=Roboto+Condensed:wght@400;700&family=Archivo+Black&display=swap">
<style>
  :root {
    --bg: #2b2b2b;
    --paper: #ffffff;
    --header-grey: #58585a;
    --orange: #ee8424;
    --ink: #1f1f1f;
    --rule: #c9c9c9;
    --dark-outline: #3a3a3a;
  }
  * { margin: 0; padding: 0; box-sizing: border-box; }
  html, body {
    width: 1200px; height: 1200px; overflow: hidden;
    background: var(--bg);
  }
  .flyer {
    position: absolute; left: 190px; top: 20px;
    width: 821px; height: 1160px;
    background: var(--paper);
    overflow: hidden;
    font-family: "Roboto Condensed", "Arial Narrow", sans-serif;
    color: var(--ink);
    box-shadow: 0 8px 30px rgba(0,0,0,.5);
  }
  .flyer__art { position: absolute; inset: 0; }
  .headline {
    position: absolute; left: 0; top: 0; width: 821px; height: 100px;
    background: var(--header-grey);
    color: #fff; font-weight: 700; font-size: 76px; line-height: 100px;
    text-align: center; letter-spacing: -1px;
  }
  .brand {
    position: absolute; left: 22px; top: 100px; width: 304px; height: 127px;
    background: var(--orange);
    border: 3px solid var(--dark-outline); border-top: none;
    border-radius: 0 0 18px 18px;
    display: flex; flex-direction: column; justify-content: center; align-items: center;
    color: #fff; font-weight: 700; font-size: 34px; line-height: 1.1;
    text-align: center; letter-spacing: 2px;
  }
  .open-day {
    position: absolute; left: 28px; top: 252px; width: 400px;
    color: #fff; text-shadow: 0 1px 4px rgba(0,0,0,.55);
  }
  .open-day__fee {
    display: inline-block; background: var(--orange); color: var(--ink); text-shadow: none;
    font-weight: 700; font-size: 26px; line-height: 40px; padding: 0 14px; border-radius: 8px;
  }
  .open-day__title { font-weight: 700; font-size: 32px; line-height: 1.1; margin-top: 14px; }
  .open-day__welcome { font-size: 20px; margin-top: 2px; }
  .open-day__list { list-style: none; margin-top: 8px; font-size: 19px; line-height: 27px; }
  .open-day__list li::before { content: "✓ "; font-weight: 700; color: var(--orange); }
  .offer { position: absolute; left: 29px; top: 722px; width: 400px; }
  .offer__title {
    font-family: "Archivo Black", sans-serif; font-size: 34px; letter-spacing: 1px;
    padding-bottom: 2px; border-bottom: 5px solid var(--rule); width: 380px;
  }
  .offer__list { list-style: none; margin-top: 4px; }
  .offer__list li {
    position: relative; padding-left: 26px; font-size: 21px; height: 40px; line-height: 36px;
    width: 450px;
    background: linear-gradient(90deg, var(--rule), rgba(201,201,201,0)) left bottom / 100% 4px no-repeat;
  }
  .offer__list li::before {
    content: ""; position: absolute; left: 4px; top: 15px;
    width: 7px; height: 7px; border-radius: 50%; background: var(--ink);
  }
  .quickstart {
    position: absolute; left: 501px; top: 868px; width: 296px; height: 196px;
    background: var(--orange); border-radius: 40px;
    display: flex; flex-direction: column; justify-content: center; align-items: center;
    font-weight: 700; font-size: 50px; line-height: 1.07; text-align: center; color: var(--ink);
  }
  .contact-bar {
    position: absolute; left: 0; top: 1078px; width: 821px; height: 82px;
    background: var(--orange); color: var(--ink); text-align: center;
    display: flex; flex-direction: column; justify-content: center;
  }
  .contact-bar__main { font-weight: 700; font-size: 35px; line-height: 40px; }
  .contact-bar__details { font-size: 18px; line-height: 24px; }
</style>
</head>
<body>
  <main class="flyer">
    <svg class="flyer__art" width="821" height="1160" viewBox="0 0 821 1160">
      <defs>
        <linearGradient id="gymPhotoTone" x1="0" y1="0" x2="1" y2="1">
          <stop offset="0" stop-color="#bfb3a5"/>
          <stop offset="0.5" stop-color="#96694d"/>
          <stop offset="1" stop-color="#4a4440"/>
        </linearGradient>
        <linearGradient id="stillLifeTone" x1="0" y1="0" x2="1" y2="1">
          <stop offset="0" stop-color="#dfe6ee"/>
          <stop offset="0.55" stop-color="#9bb3c6"/>
          <stop offset="1" stop-color="#5c7d3a"/>
        </linearGradient>
      </defs>
      <path d="M0 100 H821 V392 Q640 560 437 642 Q220 720 0 624 Z"
            fill="none" stroke="#b9b9b9" stroke-width="6" transform="translate(0,8)"/>
      <path class="hero-photo" role="img" aria-label="Athletic woman doing a mountain-climber exercise on a mat in a bright gym"
            d="M0 100 H821 V392 Q640 560 437 642 Q220 720 0 624 Z" fill="url(#gymPhotoTone)"/>
      <circle class="detail-photo" role="img" aria-label="Water bottle, dumbbell, fresh vegetables and a measuring tape"
              cx="638" cy="665" r="200" fill="url(#stillLifeTone)" stroke="var(--orange)" stroke-width="12"/>
    </svg>

    <h1 class="headline">HUGE MEMBERSHIP SALE</h1>

    <div class="brand">
      <span>PACER FITNESS</span>
      <span>ASHGROVE</span>
    </div>

    <section class="open-day">
      <span class="open-day__fee">NO JOINING FEE – JANUARY</span>
      <h2 class="open-day__title">OPEN DAY · SATURDAY 21 JANUARY</h2>
      <p class="open-day__welcome">Everyone is welcome!</p>
      <ul class="open-day__list">
        <li>Supplement samples &amp; information</li>
        <li>Free health measurements</li>
        <li>Free starter PT pack if you join on the day</li>
      </ul>
    </section>

    <section class="offer">
      <h2 class="offer__title">WHAT WE OFFER</h2>
      <ul class="offer__list">
        <li>Flexible 24/7 Gym membership option</li>
        <li>Personal training</li>
        <li>Small group training (2-4)</li>
        <li>Large group training</li>
        <li>Qulified, professional, friendly &amp; approachable staff</li>
        <li>Clean &amp; air-conditioned</li>
        <li>State of the art equipment</li>
      </ul>
    </section>

    <div class="quickstart">
      <span>FREE</span>
      <span>QUICKSTART</span>
      <span>PROGRAMS</span>
    </div>

    <footer class="contact-bar">
      <p class="contact-bar__main">www.pacerfitness.com.au | CALL US NOW 3290 4815</p>
      <p class="contact-bar__details">Unit 3, 48 Banksia Street, Ashgrove QLD · Staffed: Mon–Thur 12pm–7pm · Fri–Sat 8am–1pm</p>
    </footer>
  </main>
</body>
</html>
```